Postcard for Real estate agent

**Scroll all the way down for updates***.....
I want a postcard to send out to potential clients to list their house on the market.
I submitting a a basic proof with the info and images that I want on each side of the postcard. I do not want a white postcard
-I want the postcard sized 6" x 4" inches
I want my phone number to stand out
I want a PHD and Homewarden log on my postcard .Ive included examples of logos.
Feel free toe crop or enhance the images
Must look professional
-----------------------------------------------------------------------
UPDATE : August 4 , 2015 8pm Pacific Daylight Time , UTC -7
I submitted a proof of postcard I designed myself (see File 10)
Please use that for the front of the postcard.
For the back please refine the back to make it look professional
(see example of File 11 )
-----------------------------------------------------------------------------------------------------------
UPDATE: August 5 12:45 pm Pacific Daylight Time (UTC -7)
Please use Files 12, 13 and 14 on the front. No generic pictures.
You may crop and enhance my images if needed.
On the back, bottom of the postcard must have "If you are listed with another broker please disregard this mailing. This is not a solicitation"
UPDATE: August 5 12:45 pm Pacific Daylight Time (UTC -7)-------------------------------------------------------------------------------------Please use new Files 12, 13 and 14 on the front. No generic pictures.You may crop and enhance my images if needed.On the back, bottom of the postcard must have "If you are listed with another broker please disregard this mailing. This is not a solicitation"Upper left must have return address : 482 Pellmore Ave #C Avalon CA 90617-5083 Added Wednesday, August 5, 2015
Homeowners wanting to sell their property
Real Estate Agent
- My name and phone number highly visible
- Homewarden/ PHD logo
- Nothing pink, purple, lavender, brown , no pastels

```html
<!DOCTYPE html>
<html lang="en">
<head>
<meta charset="utf-8">
<title>Maren Castell – Listing Postcard</title>
<link rel="stylesheet" href="https://fonts.googleapis.com/css2?family=Bebas+Neue&family=Roboto+Condensed:ital,wght@0,400;0,700;1,400&display=swap">
<style>
  :root {
    --page: #d9d6d2;
    --red: #c1262c;
    --red-dark: #9e1d22;
    --charcoal: #3b3c40;
    --charcoal-deep: #2c2d30;
    --light: #e9e9ea;
    --white: #ffffff;
    --ink: #333438;
    --stamp: #cfcfd1;
  }
  * { box-sizing: border-box; margin: 0; padding: 0; }
  html, body { width: 900px; height: 1200px; overflow: hidden; }
  body {
    background: var(--page);
    font-family: "Roboto Condensed", Arial, sans-serif;
    position: relative;
  }
  .card {
    position: absolute;
    left: 50px;
    width: 800px;
    height: 533px;
    overflow: hidden;
    box-shadow: 0 6px 18px rgba(0,0,0,.25);
  }
  .card--front { top: 40px; background: var(--white); }
  .card--back { top: 627px; background: var(--light); }

  .display { font-family: "Bebas Neue", Impact, sans-serif; letter-spacing: .5px; }

  /* Front */
  .front__headline {
    position: absolute; left: 0; top: 0; width: 305px; height: 92px;
  }
  .front__headline svg { position: absolute; inset: 0; }
  .front__headline h2 {
    position: absolute; left: 0; top: 16px; width: 305px;
    text-align: center; color: var(--ink);
    font-size: 36px; font-weight: 400; white-space: nowrap;
  }
  .front__agent {
    position: absolute; left: 0; top: 92px; width: 305px; height: 248px;
    background: var(--red); color: var(--white); padding: 26px 22px 0;
  }
  .front__agent .name { font-size: 50px; line-height: 1; white-space: nowrap; }
  .front__agent .brokerage { font-size: 30px; line-height: 1.1; margin-top: 2px; white-space: nowrap; }
  .front__agent .location { font-size: 21px; margin-top: 14px; white-space: nowrap; }
  .front__agent .call {
    display: inline-block; margin-top: 18px;
    border: 2px solid var(--white); border-radius: 6px;
    padding: 5px 10px; font-size: 17px; font-weight: 700;
    white-space: nowrap;
  }
  .photo { position: absolute; }
  .photo--hero {
    left: 312px; top: 6px; width: 482px; height: 334px;
    background: linear-gradient(180deg, #3f86c9 0%, #8fb7d8 32%, #c9a27b 55%, #2fa6d6 78%, #6e6356 100%);
  }
  .photo-row { position: absolute; left: 0; top: 346px; width: 800px; height: 144px; }
  .photo--garage { left: 0; top: 0; width: 196px; height: 144px;
    background: linear-gradient(180deg, #6aa0d2 0%, #d9d4c8 45%, #5f7a4a 100%); }
  .photo--street { left: 202px; top: 0; width: 196px; height: 144px;
    background: linear-gradient(180deg, #8cb4d6 0%, #4f6e3c 50%, #7b7468 100%); }
  .photo--sign { left: 404px; top: 0; width: 196px; height: 144px;
    background: linear-gradient(180deg, #9fbcd4 0%, #4f7a3e 55%, #8a8175 100%); }
  .photo--harbor { left: 606px; top: 0; width: 194px; height: 144px;
    background: linear-gradient(180deg, #8ab3d9 0%, #5d8fb0 50%, #c9c2b4 100%); }
  .front__footer {
    position: absolute; left: 0; bottom: 0; width: 800px; height: 43px;
    background: var(--charcoal);
  }

  /* Back */
  .back__panel { position: absolute; left: 0; width: 380px; }
  .back__return {
    top: 22px; height: 128px; background: var(--red); color: var(--white);
    padding: 22px 22px 0; font-size: 42px; line-height: 1.02; white-space: nowrap;
  }
  .back__contact {
    top: 150px; height: 184px; background: var(--charcoal); color: var(--white);
    padding: 20px 22px 0;
  }
  .back__contact .name { color: #e0353b; font-size: 32px; line-height: 1; }
  .back__contact .phone { font-size: 42px; line-height: 1; margin-top: 6px; }
  .back__contact .email { font-size: 31px; line-height: 1; margin-top: 16px; white-space: nowrap; }
  .back__portrait {
    position: absolute; left: 276px; top: 14px; width: 88px; height: 88px;
    border-radius: 50%; border: 4px solid var(--white);
    background: radial-gradient(circle at 50% 40%, #e7c9a6 0%, #c9a46f 45%, #6b8cad 100%);
  }
  .back__office {
    top: 344px; height: 52px; background: var(--red); color: var(--white);
    padding: 10px 22px 0; font-size: 32px; line-height: 1; white-space: nowrap;
  }
  .back__credentials {
    top: 396px; height: 86px; background: var(--charcoal); color: var(--white);
    display: flex; align-items: center; gap: 16px; padding: 0 22px;
  }
  .affiliation { display: flex; align-items: center; gap: 6px;
    font-family: "Roboto Condensed", Arial, sans-serif; font-weight: 700; font-size: 15px; color: var(--white); }
  .affiliation .mark { width: 16px; height: 16px; background: var(--white); }
  .back__credentials .license { font-size: 24px; margin-left: auto; white-space: nowrap; }
  .stamp-box {
    position: absolute; left: 652px; top: 30px; width: 112px; height: 112px;
    background: var(--stamp);
  }
  .disclaimer {
    position: absolute; left: 470px; top: 452px; width: 310px;
    font-size: 12px; font-style: italic; color: var(--ink); text-align: center; line-height: 1.3;
  }
</style>
</head>
<body>

<section class="card card--front" aria-label="Postcard front">
  <div class="front__headline">
    <svg width="305" height="92" viewBox="0 0 305 92" aria-hidden="true">
      <polygon points="0,0 305,0 305,74 165,74 152,88 139,74 0,74" fill="#e9e9ea"/>
      <rect x="0" y="74" width="305" height="18" fill="#c1262c"/>
      <polygon points="139,74 165,74 152,88" fill="#e9e9ea"/>
    </svg>
    <h2 class="display">Thinking of Selling?</h2>
  </div>
  <div class="front__agent">
    <div class="name display">Maren Castell</div>
    <div class="brokerage display">Harbor Isle Realty</div>
    <div class="location">In the post office arcade</div>
    <div class="call">Call me today (310) 555-0148</div>
  </div>
  <div class="photo photo--hero" role="img" aria-label="Photo of a hillside villa with terraces and a swimming pool"></div>
  <div class="photo-row">
    <div class="photo photo--garage" role="img" aria-label="Photo of a home with a garage"></div>
    <div class="photo photo--street" role="img" aria-label="Photo of a residential street with houses and trees"></div>
    <div class="photo photo--sign" role="img" aria-label="Photo of a house with a for-sale sign in the yard"></div>
    <div class="photo photo--harbor" role="img" aria-label="Photo of the agent standing by the harbor"></div>
  </div>
  <div class="front__footer"></div>
</section>

<section class="card card--back" aria-label="Postcard back">
  <div class="back__panel back__return display">482 Pellmore Ave. #C<br>Avalon, CA 90617-5083</div>
  <div class="back__panel back__contact display">
    <div class="name">Maren Castell</div>
    <div class="phone">(310) 555-0148</div>
    <div class="email">salesbymaren@mailbox.com</div>
    <div class="back__portrait" role="img" aria-label="Portrait photo of the agent"></div>
  </div>
  <div class="back__panel back__office display">In the Post Office Arcade</div>
  <div class="back__panel back__credentials">
    <div class="affiliation"><span class="mark"></span>Homewarden</div>
    <div class="affiliation"><span class="mark"></span>PHD</div>
    <div class="license display">BRE# 02736145</div>
  </div>
  <div class="stamp-box" aria-label="Postage area"></div>
  <p class="disclaimer">"If you are listed with another broker please disregard this mailing. This is not a solicitation"</p>
</section>

</body>
</html>
```